Business card design needed

Need a new business card design for a new business in Sydney, Australia called 'Tarrow Australia'. The business deals in consulting for new sales, sales leadership and customer service consultancy. Want the business card to look professional and clean

Industry/Entity Type

Leadership

Contact Information for Business Card

Tarrow Australia
Peter Holm
Managing Director

14 Corvane Street
Brackmere NSW 2095

0455 913 702
peter@tarrow.com.au
www.tarrow.com.au

```html
<!DOCTYPE html>
<html lang="en">
<head>
<meta charset="utf-8">
<title>Tarrow Australia – Business Card</title>
<link rel="stylesheet" href="https://fonts.googleapis.com/css2?family=Barlow:wght@300;400;500&display=swap">
<style>
  :root {
    --page: #ffffff;
    --card-black: #050607;
    --card-deep: #0d1216;
    --slate: #2c3945;
    --slate-light: #3a4957;
    --ink: #ffffff;
    --shadow: rgba(0, 0, 0, 0.55);
  }
  html, body {
    margin: 0;
    padding: 0;
    width: 1200px;
    height: 764px;
    overflow: hidden;
    background: var(--page);
  }
  .canvas {
    position: relative;
    width: 1200px;
    height: 764px;
    font-family: "Barlow", sans-serif;
    color: var(--ink);
  }
  .card-shadow {
    position: absolute;
    left: 136px;
    top: 125px;
    width: 948px;
    height: 533px;
    background: var(--shadow);
    filter: blur(3px);
  }
  .card {
    position: absolute;
    left: 126px;
    top: 115px;
    width: 948px;
    height: 533px;
    overflow: hidden;
    background: var(--card-black);
  }
  .card-waves {
    position: absolute;
    inset: 0;
    width: 100%;
    height: 100%;
  }
  .text {
    position: absolute;
    margin: 0;
    white-space: nowrap;
    line-height: 1;
  }
  .brand {
    left: 564px;
    top: 78px;
    width: 332px;
    text-align: center;
    font-weight: 500;
  }
  .brand-name {
    display: block;
    font-size: 80px;
    letter-spacing: 0.5px;
  }
  .brand-region {
    display: block;
    font-size: 68px;
    margin-top: 2px;
    letter-spacing: 1px;
  }
  .brand-rule {
    position: absolute;
    left: 535px;
    top: 233px;
    width: 330px;
    height: 2px;
    background: var(--ink);
  }
  .website {
    left: 535px;
    top: 244px;
    width: 330px;
    text-align: center;
    font-size: 26px;
    font-weight: 400;
    letter-spacing: 0.5px;
  }
  .person {
    left: 58px;
    top: 218px;
    width: 318px;
    text-align: center;
  }
  .person-name {
    display: block;
    font-size: 43px;
    font-weight: 300;
    letter-spacing: 0.5px;
  }
  .person-role {
    display: block;
    font-size: 26px;
    font-weight: 400;
    margin-top: 10px;
    letter-spacing: 0.5px;
  }
  .contact {
    left: 40px;
    top: 426px;
    font-size: 40px;
    font-weight: 300;
    line-height: 46px;
    letter-spacing: 0.3px;
  }
  .address {
    right: 38px;
    top: 426px;
    text-align: right;
    font-size: 40px;
    font-weight: 300;
    line-height: 46px;
    letter-spacing: 0.3px;
    font-style: normal;
  }
</style>
</head>
<body>
<main class="canvas">
  <div class="card-shadow"></div>
  <section class="card" aria-label="Tarrow Australia business card">
    <svg class="card-waves" viewBox="0 0 948 533" preserveAspectRatio="none" aria-hidden="true">
      <defs>
        <linearGradient id="topWave" x1="0" y1="0" x2="1" y2="0">
          <stop offset="0" stop-color="#111920"/>
          <stop offset="0.45" stop-color="#1f2a33"/>
          <stop offset="1" stop-color="#2c3945"/>
        </linearGradient>
        <linearGradient id="sweepBand" x1="0" y1="0" x2="1" y2="0">
          <stop offset="0" stop-color="#2c3945"/>
          <stop offset="0.35" stop-color="#3a4957"/>
          <stop offset="0.6" stop-color="#0d1216"/>
        </linearGradient>
        <linearGradient id="bottomWave" x1="0" y1="0" x2="1" y2="0">
          <stop offset="0" stop-color="#2c3945"/>
          <stop offset="0.55" stop-color="#1d262e"/>
          <stop offset="1" stop-color="#2c3945"/>
        </linearGradient>
        <radialGradient id="centreGlow" cx="0.4" cy="0.7" r="0.6">
          <stop offset="0" stop-color="#1a232b"/>
          <stop offset="1" stop-color="#050607" stop-opacity="0"/>
        </radialGradient>
      </defs>
      <rect width="948" height="533" fill="var(--card-black)"/>
      <rect width="948" height="533" fill="url(#centreGlow)"/>
      <path d="M0 0 H948 V110 C760 50 560 50 300 100 C180 124 80 142 0 160 Z" fill="url(#topWave)"/>
      <path d="M0 160 C120 132 220 112 320 98 C230 122 130 150 0 180 Z" fill="url(#sweepBand)"/>
      <path d="M0 418 C260 420 620 390 948 336 V372 C700 430 420 455 0 445 Z" fill="url(#bottomWave)"/>
    </svg>

    <h1 class="text brand">
      <span class="brand-name">Tarrow</span>
      <span class="brand-region">Australia</span>
    </h1>
    <div class="brand-rule"></div>
    <p class="text website">www.tarrow.com.au</p>

    <p class="text person">
      <span class="person-name">Peter Holm</span>
      <span class="person-role">managing director</span>
    </p>

    <p class="text contact">0455 913 702<br>peter@tarrow.com.au</p>

    <address class="text address">14 Corvane Street<br>Brackmere NSW 2095</address>
  </section>
</main>
</body>
</html>
```